Wine Bottle Lable

Want a unique, simple but elegant, label for a wine bottle. I want to use the letters "DKP" in the design which is a moniker for my last name "Dufkamp". The letters DKP do not have to be juxtaposed together so that it is recognizable, or they could be something like D-KP, KP-D, DPK D-KP-D, etc. The X could be totally separated from the NO, or otherwise. The wine is a white wine in a clear bottle. I need Adobe Illustrator files so I can add the wine varietal, year, alcohol content. The label should be 4" wide and 5" tall.

Colors

Designer to choose colors to be used in the design.

Requirements
Nice to have
• outstanding but simple graphics

```html
<!DOCTYPE html>
<html lang="en">
<head>
<meta charset="utf-8">
<title>Dufkamp Wine Label</title>
<link rel="stylesheet" href="https://fonts.googleapis.com/css2?family=Roboto+Condensed:wght@700&family=Saira:wght@300;500&family=Noto+Serif:wght@700&display=swap">
<style>
  :root {
    --backdrop: #182536;
    --label-grey: #454647;
    --band-white: #f4f4f2;
    --ink-white: #f2f2f0;
    --ink-soft: #c9c9c9;
    --ink-muted: #8e8f90;
  }
  html, body {
    margin: 0;
    width: 1200px;
    height: 860px;
    overflow: hidden;
    background: var(--backdrop);
  }
  .stage {
    position: relative;
    width: 1200px;
    height: 860px;
    display: flex;
    align-items: center;
    justify-content: center;
  }
  .wine-label {
    position: relative;
    width: 560px;
    height: 700px;
    background: var(--label-grey);
    box-sizing: border-box;
    overflow: hidden;
  }
  .band {
    position: absolute;
    left: 0;
    right: 0;
    height: 22px;
    background: var(--band-white);
  }
  .band--top { top: 34px; }
  .band--bottom { bottom: 34px; }
  .winery-name {
    position: absolute;
    left: 70px;
    top: 200px;
    margin: 0;
    font-family: "Roboto Condensed", "Arial Narrow", sans-serif;
    font-weight: 700;
    font-size: 46px;
    color: var(--ink-soft);
    letter-spacing: 0.5px;
  }
  .monogram {
    position: absolute;
    left: 60px;
    right: 60px;
    top: 290px;
    display: flex;
    justify-content: space-between;
    font-family: "Saira", "Arial", sans-serif;
    font-weight: 500;
    font-size: 150px;
    line-height: 1;
  }
  .monogram__letter { color: var(--ink-white); }
  .monogram__letter--muted { color: var(--ink-soft); }
  .vintage {
    position: absolute;
    left: 235px;
    top: 470px;
    font-family: "Saira", "Arial", sans-serif;
    font-weight: 300;
    font-size: 38px;
    letter-spacing: 30px;
    color: var(--ink-white);
  }
  .alcohol {
    position: absolute;
    right: 36px;
    bottom: 78px;
    font-family: "Noto Serif", Georgia, serif;
    font-weight: 700;
    font-size: 28px;
    color: var(--ink-white);
  }
  .ornament {
    position: absolute;
    width: 40px;
    height: 26px;
  }
  .ornament--top { right: 70px; top: 90px; }
  .ornament--left { left: 30px; top: 420px; }
  .ornament--right { right: 30px; top: 420px; }
</style>
</head>
<body>
<main class="stage">
  <article class="wine-label">
    <div class="band band--top"></div>

    <svg class="ornament ornament--top" role="img" aria-label="Small manta ray ornament" viewBox="0 0 40 26">
      <rect width="40" height="26" rx="6" fill="#e8e8e6"/>
    </svg>

    <h1 class="winery-name">Dufkamp</h1>

    <div class="monogram" aria-label="DKP">
      <span class="monogram__letter monogram__letter--muted">K</span>
      <span class="monogram__letter">D</span>
      <span class="monogram__letter">P</span>
    </div>

    <svg class="ornament ornament--left" role="img" aria-label="Small manta ray ornament" viewBox="0 0 40 26">
      <rect width="40" height="26" rx="6" fill="#e8e8e6"/>
    </svg>
    <svg class="ornament ornament--right" role="img" aria-label="Small manta ray ornament" viewBox="0 0 40 26">
      <rect width="40" height="26" rx="6" fill="#e8e8e6"/>
    </svg>

    <p class="vintage">1992</p>

    <p class="alcohol">Alc. 14.5% Vol</p>

    <div class="band band--bottom"></div>
  </article>
</main>
</body>
</html>
```